Kelo8Ventra Roadmap for developing engineer 3D-BIM-projects over a longer period of time

We need functional and scalable PowerPoint templates with four main slides. The design should be carried out in the context of the enclosed documents; or at least in this sense.
As engineers, we develop projects over a longer period of time. To visualize topics along the way (downside timeline) and goals (upside timeline) for our customers (and for us), we need an overview for the project management in sort of a roadmap.
Our design requirements are simplicity, clarity and accuracy. These are also the service requirements for our customers.
As always, it's urgent. Our goal is to select the design by Wednesday November 10th and make any adjustments with the winner by Friday November 12th.

Target Market(s)

Architects, Engineers, World Heritage; 3D-Modelling, BIM Building Information Modeling

Industry/Entity Type

World Heritage Buildings and Objects

Requirements
Must have
• simplicity, logic, elegant (see the attached documents)
Nice to have
• see the attached documents

```html
<!DOCTYPE html>
<html lang="de">
<head>
<meta charset="utf-8">
<title>Kelo8Ventra – Roadmap Templates</title>
<link href="https://fonts.googleapis.com/css2?family=Bebas+Neue&family=Open+Sans:wght@400;700&display=swap" rel="stylesheet">
<style>
  :root{
    --stage-light:#e2e2e2;
    --stage-dark:#b9b9b9;
    --brand-blue:#0a64b6;
    --brand-blue-deep:#0850a0;
    --brand-blue-soft:#0d74c4;
    --brand-red:#ef4023;
    --bar-blue:#1ea6ec;
    --white:#ffffff;
  }
  html,body{margin:0;padding:0;overflow:hidden;}
  body{
    width:1200px;height:746px;position:relative;
    background:radial-gradient(ellipse at center,var(--stage-light) 0%,var(--stage-dark) 100%);
    font-family:"Open Sans",Arial,sans-serif;
  }
  .slide{
    position:absolute;display:block;
    box-shadow:3px 4px 6px rgba(0,0,0,.45);
  }
  .slide--title{left:45px;top:41px;width:536px;height:302px;}
  .slide--kickoff{left:624px;top:36px;width:528px;height:303px;}
  .slide--roadmap{left:45px;top:373px;width:536px;height:302px;}
  .slide--topic{left:624px;top:376px;width:528px;height:303px;}
  .display{font-family:"Bebas Neue","Oswald",sans-serif;}
  .copy{font-family:"Open Sans",Arial,sans-serif;}
  .fill-blue{fill:var(--brand-blue);}
  .fill-deep{fill:var(--brand-blue-deep);}
  .fill-soft{fill:var(--brand-blue-soft);}
  .fill-red{fill:var(--brand-red);}
  .fill-white{fill:var(--white);}
  .fill-bar{fill:var(--bar-blue);}
  .outline-red{fill:none;stroke:var(--brand-red);stroke-width:3;}
  .timeline-line{stroke:var(--white);stroke-width:2;}
  .timeline-node{fill:none;stroke:var(--white);stroke-width:2.5;}
  .timeline-dot{fill:var(--white);}
  .month{font-family:"Open Sans",Arial,sans-serif;font-weight:700;font-size:10px;fill:var(--white);text-anchor:middle;}
  .heading{font-weight:700;font-size:16px;fill:var(--white);}
  .body{font-size:12.5px;fill:var(--white);}
  .milestone-label{font-family:"Bebas Neue",sans-serif;font-size:17px;fill:var(--brand-blue);text-anchor:middle;letter-spacing:.3px;}
  .task-label{font-size:8.5px;fill:var(--white);}
</style>
</head>
<body>

<!-- Title slide -->
<svg class="slide slide--title" viewBox="0 0 715 403" role="group" aria-label="Titelfolie">
  <rect width="715" height="403" class="fill-blue"/>
  <polygon points="420,123 715,123 715,403 560,403" class="fill-soft" opacity=".55"/>
  <polygon points="580,260 715,160 715,403 640,403" class="fill-deep" opacity=".5"/>
  <rect width="715" height="123" class="fill-white"/>
  <polygon points="605,0 715,0 715,70" class="fill-red"/>
  <polygon points="0,62 125,123 0,186" class="fill-red"/>
  <polygon points="32,60 160,123 32,188" class="outline-red"/>
  <rect x="287" y="38" width="10" height="10" class="fill-red"/>
  <text x="287" y="100" class="display" font-size="44" fill="#0a64b6">Kelo8Ventra</text>
  <text x="355" y="222" class="display" font-size="40" fill="#fff" text-anchor="middle" letter-spacing="1">PROJECT NAME</text>
  <text class="copy body" font-size="11"><tspan x="160" y="312">Lorem ipsum dolor sit amet, consectetur adipiscing elit. Fusce lobortis luctus purus,</tspan><tspan x="160" y="325">imperdiet rhoncus mauris sagittis nec. Duis egestas blandit odio at efficitur.</tspan></text>
</svg>

<!-- Kick-off slide -->
<svg class="slide slide--kickoff" viewBox="0 0 704 404" role="group" aria-label="Meilenstein Kick-off">
  <rect width="704" height="404" class="fill-blue"/>
  <polygon points="420,0 704,0 704,404 620,404" class="fill-deep" opacity=".35"/>
  <polygon points="0,28 112,82 0,140" class="fill-red"/>
  <polygon points="20,17 150,82 20,147" class="outline-red"/>
  <text x="169" y="86" class="copy heading">Lorem ipsum dolor</text>
  <text class="copy body">
    <tspan x="169" y="116">sit amet, consectetur adipiscing elit. Fusce lobortis luctus purus,</tspan>
    <tspan x="169" y="131">imperdiet rhoncus mauris sagittis nec. Duis egestas blandit odio</tspan>
    <tspan x="169" y="146">at efficitur. Mauris dictum pretium odio, id sollicitudin dui maxi-</tspan>
    <tspan x="169" y="161">mus nec. Sed feugiat gravida nisi non maximus. Phasellus sem</tspan>
    <tspan x="169" y="177">mi, porta id feugiat eu, dapibus id arcu. Integer in lacus faucibus,</tspan>
    <tspan x="169" y="192">fermentum neque ac, mattis nisi. Aliquam ante magna, sodales</tspan>
    <tspan x="169" y="207">vitae sagittis sit amet.</tspan>
  </text>
  <rect y="259" width="704" height="68" class="fill-white"/>
  <polygon points="333,259 353,228 373,259" class="fill-white"/>
  <rect x="273" y="270" width="155" height="45" class="fill-red"/>
  <text x="351" y="307" class="display" font-size="38" fill="#fff" text-anchor="middle">KICK-OFF</text>
  <line x1="72" y1="354" x2="628" y2="354" class="timeline-line"/>
  <polygon points="66,354 78,348 78,360" class="fill-white"/>
  <polygon points="636,354 624,348 624,360" class="fill-white"/>
  <g>
    <circle cx="184" cy="354" r="9" class="timeline-node" fill="#0a64b6"/><circle cx="184" cy="354" r="3.5" class="timeline-dot"/>
    <circle cx="286" cy="354" r="9" class="timeline-node"/><circle cx="286" cy="354" r="3.5" class="timeline-dot"/>
    <circle cx="440" cy="354" r="9" class="timeline-node"/><circle cx="440" cy="354" r="3.5" class="timeline-dot"/>
    <circle cx="536" cy="354" r="9" class="timeline-node"/><circle cx="536" cy="354" r="3.5" class="timeline-dot"/>
  </g>
  <text x="182" y="386" class="month">APR</text>
  <text x="285" y="386" class="month">JUN</text>
  <text x="441" y="386" class="month">NOV</text>
  <text x="535" y="386" class="month">DEZ</text>
</svg>

<!-- Roadmap overview slide -->
<svg class="slide slide--roadmap" viewBox="0 0 715 403" role="group" aria-label="Roadmap Übersicht">
  <rect width="715" height="403" class="fill-blue"/>
  <polygon points="330,0 715,0 715,278 600,403 520,403" class="fill-deep" opacity=".3"/>
  <polygon points="0,20 125,82 0,145" class="fill-red"/>
  <polygon points="32,17 160,82 32,147" class="outline-red"/>

  <line x1="72" y1="216" x2="628" y2="216" class="timeline-line"/>
  <polygon points="66,216 78,210 78,222" class="fill-white"/>
  <polygon points="636,216 624,210 624,222" class="fill-white"/>

  <g class="milestone">
    <line x1="185" y1="110" x2="185" y2="207" class="timeline-line"/>
    <polygon points="185,110 205,119 185,128" class="fill-red"/>
    <rect x="152" y="139" width="63" height="20" class="fill-white"/>
    <text x="183.5" y="156" class="milestone-label">KICK-OFF</text>
  </g>
  <g class="milestone">
    <line x1="287" y1="79" x2="287" y2="207" class="timeline-line"/>
    <polygon points="287,79 307,88 287,97" class="fill-red"/>
    <rect x="243" y="108" width="92" height="20" class="fill-white"/>
    <text x="289" y="125" class="milestone-label">DATENBANKEN</text>
  </g>
  <g class="milestone">
    <line x1="441" y1="69" x2="441" y2="207" class="timeline-line"/>
    <polygon points="441,69 461,78 441,87" class="fill-red"/>
    <rect x="415" y="98" width="59" height="19" class="fill-white"/>
    <text x="444.5" y="114" class="milestone-label">MOCK-UP</text>
  </g>
  <g class="milestone">
    <line x1="537" y1="57" x2="537" y2="207" class="timeline-line"/>
    <polygon points="537,57 557,66 537,75" class="fill-red"/>
    <rect x="494" y="86" width="97" height="20" class="fill-white"/>
    <text x="542.5" y="103" class="milestone-label">ROADMAP2022</text>
  </g>

  <g>
    <circle cx="185" cy="216" r="9" class="timeline-node" fill="#0a64b6"/><circle cx="185" cy="216" r="3.5" class="timeline-dot"/>
    <circle cx="287" cy="216" r="9" class="timeline-node" fill="#0a64b6"/><circle cx="287" cy="216" r="3.5" class="timeline-dot"/>
    <circle cx="441" cy="216" r="9" class="timeline-node" fill="#0a64b6"/><circle cx="441" cy="216" r="3.5" class="timeline-dot"/>
    <circle cx="537" cy="216" r="9" class="timeline-node" fill="#0a64b6"/><circle cx="537" cy="216" r="3.5" class="timeline-dot"/>
  </g>
  <text x="183" y="248" class="month">APR</text>
  <text x="286" y="248" class="month">JUN</text>
  <text x="442" y="248" class="month">NOV</text>
  <text x="536" y="248" class="month">DEZ</text>

  <g class="copy">
    <text x="128" y="271" class="task-label">Laserscanning</text>
    <rect x="124" y="272" width="104" height="4" class="fill-bar"/>
    <text x="172" y="288" class="task-label">Drohne</text>
    <rect x="169" y="293" width="59" height="4" class="fill-bar"/>
    <text x="263" y="305" class="task-label">Datenprozessierung</text>
    <rect x="216" y="308" width="330" height="4" class="fill-bar"/>
    <text x="296" y="322" class="task-label">Datenbankmanagementsystem</text>
    <rect x="308" y="325" width="210" height="4" class="fill-bar"/>
    <text x="415" y="339" class="task-label">3D-Modellierung</text>
    <text x="503" y="356" class="task-label">BIM-Viewer</text>
    <rect x="503" y="361" width="56" height="4" class="fill-bar"/>
  </g>

  <polygon points="715,278 715,403 588,403" class="fill-white"/>
  <text x="666" y="378" class="display" font-size="22" fill="#0a64b6">Torvik</text>
</svg>

<!-- Topic slide -->
<svg class="slide slide--topic" viewBox="0 0 704 403" role="group" aria-label="Thema Laserscanning">
  <rect width="704" height="403" class="fill-blue"/>
  <polygon points="420,0 704,0 704,403 640,403" class="fill-deep" opacity=".35"/>
  <line x1="72" y1="26" x2="628" y2="26" class="timeline-line"/>
  <polygon points="66,26 78,20 78,32" class="fill-white"/>
  <polygon points="636,26 624,20 624,32" class="fill-white"/>
  <g>
    <circle cx="184" cy="26" r="9" class="timeline-node" fill="#0a64b6"/><circle cx="184" cy="26" r="3.5" class="timeline-dot"/>
    <circle cx="286" cy="26" r="9" class="timeline-node" fill="#0a64b6"/><circle cx="286" cy="26" r="3.5" class="timeline-dot"/>
    <circle cx="440" cy="26" r="9" class="timeline-node" fill="#0a64b6"/><circle cx="440" cy="26" r="3.5" class="timeline-dot"/>
    <circle cx="536" cy="26" r="9" class="timeline-node" fill="#0a64b6"/><circle cx="536" cy="26" r="3.5" class="timeline-dot"/>
  </g>
  <text x="182" y="58" class="month">APR</text>
  <text x="285" y="58" class="month">JUN</text>
  <text x="441" y="58" class="month">NOV</text>
  <text x="535" y="58" class="month">DEZ</text>

  <rect y="76" width="704" height="67" class="fill-white"/>
  <polygon points="333,143 353,175 373,143" class="fill-white"/>
  <rect x="203" y="88" width="273" height="43" class="fill-red"/>
  <text x="339" y="124" class="display" font-size="40" fill="#fff" text-anchor="middle">LASERSCANNING</text>

  <text x="169" y="192" class="copy heading">Lorem ipsum dolor</text>
  <text class="copy body">
    <tspan x="169" y="222">sit amet, consectetur adipiscing elit. Fusce lobortis luctus purus,</tspan>
    <tspan x="169" y="237">imperdiet rhoncus mauris sagittis nec. Duis egestas blandit odio</tspan>
    <tspan x="169" y="252">at efficitur. Mauris dictum pretium odio, id sollicitudin dui maxi-</tspan>
    <tspan x="169" y="267">mus nec. Sed feugiat gravida nisi non maximus. Phasellus sem</tspan>
    <tspan x="169" y="282">mi, porta id feugiat eu, dapibus id arcu. Integer in lacus faucibus,</tspan>
    <tspan x="169" y="297">fermentum neque ac, mattis nisi. Aliquam ante magna, sodales</tspan>
    <tspan x="169" y="312">vitae sagittis sit amet.</tspan>
  </text>

  <polygon points="0,268 112,325 0,382" class="fill-red"/>
  <polygon points="20,258 150,325 20,390" class="outline-red"/>
</svg>

</body>
</html>
```